Wine Bottle Label Logo Design

My fiancé and I are getting married in September and we made homemade wine which will be given to the guests as a wedding favor. We need label/logo for our wine bottles. We were looking for something rustic yet modern and simple. We had an idea for beige and cranberry colored wine stained, weathered, imperfect heart. Things that will need to be incorporated into the label design are as follows:
Our last name and also the name of the wine: Fusaldi
The year: 2012
Where is says Alcohol Content on a wine bottle normally write: Alcohol: Deceiving% by vol.
Type of wine: Red Wine
Incorporate our wedding date: Foot Stomped and Bottled for Nadia and Gus's Wedding Day 9/28/13
Wedding

```html
<!DOCTYPE html>
<html lang="en">
<head>
<meta charset="utf-8">
<title>Fusaldi Wedding Wine Label</title>
<link rel="stylesheet" href="https://fonts.googleapis.com/css2?family=Libre+Baskerville:wght@400;700&family=Cormorant+Garamond:wght@500&display=swap">
<style>
  :root {
    --page: #ffffff;
    --label-beige: #eccf9b;
    --label-grain: rgba(120, 95, 55, 0.10);
    --ink-white: #ffffff;
    --cranberry: #6e0f1c;
    --cranberry-soft: rgba(110, 15, 28, 0.35);
  }
  html, body {
    margin: 0;
    padding: 0;
    width: 1200px;
    height: 1000px;
    overflow: hidden;
    background: var(--page);
  }
  .canvas {
    position: relative;
    width: 1200px;
    height: 1000px;
    background: var(--page);
  }
  .wine-label {
    position: absolute;
    left: 185px;
    top: 0;
    width: 803px;
    height: 1000px;
    background-color: var(--label-beige);
    background-image:
      radial-gradient(var(--label-grain) 0.8px, transparent 1.2px),
      radial-gradient(var(--label-grain) 0.8px, transparent 1.2px);
    background-size: 7px 7px, 11px 11px;
    background-position: 0 0, 3px 5px;
    color: var(--ink-white);
    font-family: "Libre Baskerville", "Palatino Linotype", Georgia, serif;
    font-weight: 700;
    text-align: center;
  }
  .line {
    position: absolute;
    left: 0;
    width: 100%;
    margin: 0;
    line-height: 1;
    white-space: nowrap;
  }
  .dedication { top: 110px; font-size: 21px; }
  .couple { top: 163px; font-size: 29px; }
  .occasion { top: 211px; font-size: 29px; }
  .wedding-date { top: 258px; font-size: 29px; }

  .heart-stain {
    position: absolute;
    left: 485px;
    top: 236px;
    width: 265px;
    height: 250px;
    border-radius: 48% 48% 40% 40%;
    background: radial-gradient(ellipse at 55% 45%, var(--cranberry-soft) 0%, rgba(110,15,28,0.12) 55%, rgba(110,15,28,0) 75%);
  }

  .wine-name {
    top: 372px;
    left: 95px;
    width: 630px;
    font-family: "Cormorant Garamond", "Times New Roman", serif;
    font-weight: 500;
    font-size: 168px;
    letter-spacing: -2px;
  }
  .vintage { top: 563px; font-size: 32px; }
  .varietal { top: 604px; font-size: 22px; }
  .tasting-note {
    position: absolute;
    top: 656px;
    left: 0;
    width: 100%;
    margin: 0;
    font-size: 21.5px;
    line-height: 38.5px;
  }
  .alcohol-content { top: 875px; font-size: 19px; word-spacing: 3px; }
</style>
</head>
<body>
<main class="canvas">
  <section class="wine-label">
    <p class="line dedication">FOOT STOMPED AND BOTTLED FOR</p>
    <p class="line couple">NADIA &amp; GUS'S</p>
    <p class="line occasion">WEDDING DAY</p>
    <p class="line wedding-date">9.28.13</p>

    <div class="heart-stain" role="img" aria-label="Cranberry wine-stain heart ring with two small drip spots"></div>

    <h1 class="line wine-name">FUSALDI</h1>

    <p class="line vintage">2012</p>
    <p class="line varietal">RED WINE</p>
    <p class="tasting-note">AGED OUTDOORS DURING THE COLD<br>WINTER MONTHS TO ALLOW FOR A SLOWER<br>FERMENTATION PROCESS.<br>ITS LIKE A WARM SWEET HUG IN A BOTTLE.</p>

    <p class="line alcohol-content">ALCOHOL: DECEIVING% BY VOL.</p>
  </section>
</main>
</body>
</html>
```